FREE DENTURES

The card will be placed on plastic stand at doctors office and Seniors centers. This is to acheive specific market segment of people that must have Evergard A & B card and FULL helpnet.
The size of the card shuold be 3.1/2" X 6" printed on vertical format. The basic design must have a picture of a denture and a eye glass frame.The content should be:
NEED DENTURES and/or EYE GLASSES?
NO COST TO YOU
Must have EVERGARD A & B and FULL HELPNET
Must qualify for program
No obligation Call today
BRAM OKUDA 555-238-0194
(Not affiliated with Norvale Union Authority, the Federal Evergard or the State Helpnet Program

Add at a proper side or top. 2 stripes, 1 Red, 1 blue in a waive format.

```html
<!DOCTYPE html>
<html lang="en">
<head>
<meta charset="utf-8">
<title>Free Dentures Card</title>
<link rel="stylesheet" href="https://fonts.googleapis.com/css2?family=Questrial&family=Arimo:wght@400&display=swap">
<style>
  :root {
    --stage: #ececea;
    --card-white: #ffffff;
    --brand-blue: #3a63b0;
    --text-blue: #2e58a8;
    --brand-red: #b51f26;
    --headline-red: #e2242c;
    --ink-grey: #3b3b3b;
    --ghost-grey: #d9d9d9;
  }
  * { margin: 0; padding: 0; box-sizing: border-box; }
  html, body { width: 1200px; height: 900px; overflow: hidden; }
  body { background: var(--stage); position: relative; font-family: "Arimo", Arial, sans-serif; }

  .card {
    position: absolute;
    top: 80px;
    width: 440px;
    height: 740px;
    background: var(--card-white);
    overflow: hidden;
    box-shadow: 0 4px 14px rgba(0,0,0,0.18);
  }

  /* Back side */
  .card--back { left: 130px; background: var(--brand-blue); }
  .silhouette-area {
    position: absolute;
    left: 18px; right: 18px; top: 0; bottom: 0;
    background: var(--card-white);
    border-radius: 170px 170px 0 0;
  }
  .requirements {
    position: absolute;
    top: 200px; left: 0; right: 0;
    text-align: center;
    color: var(--text-blue);
    font-size: 29px;
    line-height: 1.08;
    list-style: none;
  }
  .requirements li { margin-bottom: 6px; }
  .requirements li::before { content: "• "; font-size: 22px; vertical-align: 4px; }
  .call-to-action {
    position: absolute;
    top: 630px; left: 0; right: 0;
    text-align: center;
    font-family: "Questrial", "Century Gothic", sans-serif;
    color: var(--brand-red);
    font-size: 36px;
  }
  .contact-band {
    position: absolute;
    left: 0; right: 0; bottom: 0;
    height: 64px;
    background: var(--brand-red);
    color: var(--card-white);
    font-family: "Questrial", "Century Gothic", sans-serif;
    font-size: 27px;
    display: flex; align-items: center; justify-content: center;
    letter-spacing: 0.5px;
  }
  .contact-band .rep-name { margin-right: 14px; }

  /* Front side */
  .card--front { left: 640px; background: linear-gradient(180deg, #f7f7f7 0%, #ffffff 40%, #f4f4f4 100%); }
  .headline {
    position: absolute;
    top: 28px; left: 0; right: 0;
    text-align: center;
    font-size: 25px;
    line-height: 1.05;
    font-weight: 400;
  }
  .headline .blue { color: var(--text-blue); }
  .headline .red { color: var(--headline-red); }
  .headline .small { font-size: 20px; }
  .wave-stripes { position: absolute; top: 100px; left: 0; width: 440px; height: 50px; }
  .glasses-image {
    position: absolute;
    top: 205px; left: 22px;
    width: 396px; height: 110px;
    border-radius: 14px;
    background: linear-gradient(180deg, #1a1a1a 0%, #3a3a3a 60%, #eaeaea 100%);
  }
  .dentures-image {
    position: absolute;
    top: 410px; left: 100px;
    width: 265px; height: 165px;
    border-radius: 40px 40px 60px 60px;
    background: radial-gradient(ellipse at 50% 45%, #f4f1e6 0%, #eea3a5 55%, #e58a8e 80%, #f8e4e4 100%);
  }
  .offer {
    position: absolute;
    top: 652px; left: 0; right: 0;
    text-align: center;
    font-family: "Questrial", "Century Gothic", sans-serif;
    font-size: 39px;
    color: var(--ink-grey);
    letter-spacing: 0.5px;
    line-height: 1;
  }
  .offer-reflection {
    position: absolute;
    top: 690px; left: 0; right: 0;
    text-align: center;
    font-family: "Questrial", "Century Gothic", sans-serif;
    font-size: 39px;
    color: var(--ghost-grey);
    letter-spacing: 0.5px;
    line-height: 1;
    transform: scaleY(-1);
    opacity: 0.7;
  }
</style>
</head>
<body>

  <section class="card card--back">
    <div class="silhouette-area" role="img" aria-label="White head-and-shoulders silhouette on blue"></div>
    <ul class="requirements">
      <li>Must have<br>EVERGARD A &amp; B<br>and FULL HELPNET</li>
      <li>Must qualify for program</li>
      <li>No obligation</li>
    </ul>
    <p class="call-to-action">Call today</p>
    <div class="contact-band">
      <span class="rep-name">BRAM OKUDA</span>
      <span class="rep-phone">555-238-0194</span>
    </div>
  </section>

  <section class="card card--front">
    <h1 class="headline">
      <span class="blue">NEED DENTURES</span> <span class="red small">and/or</span><br>
      <span class="red">EYE GLASSES?</span>
    </h1>
    <svg class="wave-stripes" viewBox="0 0 440 50" aria-hidden="true">
      <path d="M0 22 Q220 0 440 14" fill="none" stroke="var(--headline-red)" stroke-width="6"/>
      <path d="M0 34 Q220 12 440 26" fill="none" stroke="var(--brand-blue)" stroke-width="6"/>
    </svg>
    <div class="glasses-image" role="img" aria-label="Black eyeglass frames with soft reflection"></div>
    <div class="dentures-image" role="img" aria-label="Full set of dentures"></div>
    <p class="offer">NO COST TO YOU</p>
    <p class="offer-reflection" aria-hidden="true">NO COST TO YOU</p>
  </section>

</body>
</html>
```